Flyer-Design für Zweithaar Studio
Zielgruppe
Firma LORIN Falk ist ein Zweithaar Studio. Hier erhalten Kunden individuell auf sie zugeschnittene Perücken und Toupets. Unsere Zielgruppe sind Männer und Frauen mit wenig oder keiner Kopfbehaarung oder Menschen die krankheitsbedingt unter Haarausfall leiden.
Aufgabenstellung
Bitte Vorschläge zu Anzahl Seiten und Format erstellen, aktuell haben wir noch keine Vorstellung dazu. Folgende Inhalte haben wir schon mal als Entwurf vorbereitet:
Eine Seite zum Thema Toupets mit dem Bild vom Mann:
Leiden Sie an übermäßigem Haarausfall?
Fühlen Sie sich nicht mehr 100% wohl damit und möchten gerne wieder Ihre Attraktivität und vor allem das Wohlbefinden steigern?
Dann sind Sie bei uns sehr gut aufgehoben, denn wir können Ihnen Ihr Toupet individuell auf Ihre Bedürfnisse hin z.B. Farbe, Grauanteil, Größe und Styling anpassen.
Eine Seite zum Thema Perücken mit dem Bild der Frau:
Sind Sie an einer Perücke interessiert die augenscheinlich keinen Unterschied zu gewachsenem Haar aufweist?
Dann sind Sie bei uns an der richtigen Adresse. Die langjährige Erfahrung im Zweithaar Bereich von Friseurmeisterin verspricht Ihnen optimale Beratung und ein individuell auf Sie abgestimmtes Produkt.
Bei uns erhalten Sie Zugriff auf verschiedene Modelle im gesamten Preisspektrum.
Liegt eine von Ihrem Arzt attestierte Erkrankung vor, übernimmt Ihre Krankenkasse höchstwahrscheinlich die Kosten für Ihr Zweithaar. Die Formalitäten dazu erledigen wir gerne für Sie um Ihnen unnötigen Stress zu ersparen.
Eine weitere Seite mit den besonderen Merkmalen mit dem Bild Diversity:
Mit unserer Befestigungsmethode sind Sie sehr flexibel - starker halt für jede Situation und auf Wunsch auch abnehmbar z.B. nachts beim schlafen.
Der große Vorteil unserer Befestigungsmethode liegt darin, dass Sie diese selbst umsetzen können und somit nicht jeden Monat das Studio zur Neubefestigung aufsuchen müssen. Das spart Ihnen Zeit und Geld.
Wir können Ihnen Toupets und Perücken in allen Preisklassen anbieten, in verschiedenen Farben, auf Wunsch mit Grauanteil passend zum Alter des Trägers. Unsere Friseurmeisterin Frau Kessing berät Sie gerne, natürlich unverbindlich und kostenlos.

```html
<!DOCTYPE html>
<html lang="de">
<head>
<meta charset="utf-8">
<title>LORIN Falk – Flyer Zweithaar Studio</title>
<link rel="stylesheet" href="https://fonts.googleapis.com/css2?family=Fira+Sans:ital,wght@0,300;0,400;0,500;0,600;0,800;1,400&display=swap">
<style>
:root{
  --stage:#e9e9ea;
  --grey:#7c8184;
  --grey-dark:#5f6467;
  --label:#d8d9da;
  --label-text:#6f7477;
  --paper:#f3f3f3;
  --ink:#55595c;
  --white:#ffffff;
  --cover:#262122;
  --rule:rgba(255,255,255,.7);
}
*{box-sizing:border-box;margin:0;padding:0}
html,body{width:866px;height:1200px;overflow:hidden;background:var(--stage);font-family:"Fira Sans",sans-serif;color:var(--ink)}
.spread{position:absolute;left:23px;width:820px;height:560px;display:flex;box-shadow:0 6px 18px rgba(0,0,0,.18)}
.spread--outside{top:30px}
.spread--inside{top:620px}
.panel{position:relative;width:273.33px;height:100%;overflow:hidden}
.photo{position:absolute}
.label{display:inline-block;background:var(--label);color:var(--label-text);text-transform:uppercase;font-size:9.5px;letter-spacing:.6px;padding:3px 8px;line-height:1.2}
.label-stack{display:flex;flex-direction:column;align-items:flex-start;gap:4px}
.brand{font-family:"Fira Sans",sans-serif;font-weight:600;color:var(--white);text-align:center;letter-spacing:3px;text-transform:uppercase}

/* outside left */
.panel--wig{background:var(--paper)}
.panel--wig .intro{position:absolute;left:18px;right:16px;top:22px;font-size:8px;font-weight:600;line-height:1.35;color:var(--ink)}
.panel--wig .label-stack{position:absolute;left:18px;top:60px}
.benefits{position:absolute;left:18px;right:14px;top:118px;list-style:none;display:flex;flex-direction:column;gap:14px}
.benefits li{display:flex;gap:10px;font-size:7.6px;line-height:1.4}
.benefits svg{flex:none;width:16px;height:16px}
.panel--wig .photo{left:0;right:0;bottom:0;height:230px;background:linear-gradient(135deg,#3a3633,#1f2226 55%,#2e3136)}

/* outside middle */
.panel--contact{background:var(--grey);color:var(--white)}
.panel--contact .label-stack{position:absolute;right:10px;top:22px;align-items:flex-end}
.panel--contact .brand{position:absolute;left:0;right:0;top:100px;font-size:30px;line-height:1}
.panel--contact .brand-sub{position:absolute;left:0;right:0;top:134px;text-align:center;font-size:11px;letter-spacing:4px;font-weight:600;text-transform:uppercase}
.contact{position:absolute;left:40px;right:40px;top:170px;list-style:none;text-align:center;font-size:7.4px;line-height:1.45}
.contact li{padding:6px 0;border-bottom:1px solid var(--rule)}
.contact li:last-child{border-bottom:0}
.contact svg{display:block;margin:0 auto 3px;width:10px;height:10px}
.contact b{font-weight:600}
.hours{position:absolute;left:32px;right:32px;top:418px;border:1px solid var(--rule);padding:14px 10px 8px;font-size:7.2px;line-height:1.6}
.hours h3{position:absolute;top:-6px;left:50%;transform:translateX(-50%);background:var(--grey);padding:0 6px;font-size:7.2px;font-weight:600;letter-spacing:.8px;text-transform:uppercase;white-space:nowrap}
.hours dl{display:grid;grid-template-columns:auto 1fr;column-gap:10px}
.hours dd{text-align:right}

/* outside right (cover) */
.panel--cover{background:var(--cover);color:var(--white)}
.panel--cover .photo{left:0;right:0;top:130px;bottom:0;background:radial-gradient(ellipse at 55% 45%,#8a6a55 0%,#5a4436 40%,#2a2223 80%)}
.panel--cover .brand{position:absolute;left:0;right:0;top:26px;font-size:26px;line-height:1}
.panel--cover .brand-sub{position:absolute;left:0;right:0;top:56px;text-align:center;font-size:10px;letter-spacing:4px;font-weight:600;text-transform:uppercase}
.cover-title{position:absolute;left:0;right:0;top:80px;text-align:center;font-weight:800;font-size:19px;line-height:1.05;text-transform:uppercase}
.cover-title small{font-size:8px;font-weight:600;vertical-align:top}
.cover-sub{position:absolute;left:0;right:0;top:126px;text-align:center;font-size:8px;font-weight:300;letter-spacing:.4px;z-index:1}
.panel--cover .label-stack{position:absolute;right:10px;top:360px;align-items:flex-end;z-index:1}
.panel--cover .label{font-size:11px}
.cover-web{position:absolute;right:14px;bottom:14px;font-size:8px;letter-spacing:.4px;z-index:1}

/* inside: hero photo spans left and middle panels only */
.photo--hero{left:0;top:0;width:546.66px;height:255px;background:radial-gradient(ellipse at 55% 55%,#7a2e25 0%,#3b1c1b 35%,#1f1d21 70%);z-index:2}
.panel--toupet{background:var(--paper)}
.questions{position:absolute;left:16px;right:10px;top:266px;display:flex;flex-direction:column;gap:6px}
.questions .label{font-size:9px;background:#e2e3e4}
.fit{position:absolute;left:0;right:0;bottom:0;height:148px;background:var(--grey);color:var(--white);padding:14px 20px}
.fit p{font-size:8px;font-weight:600;line-height:1.35;margin-bottom:12px}
.features{list-style:none;display:grid;grid-template-columns:1fr 1fr;gap:12px 10px}
.features li{display:flex;align-items:center;gap:7px;font-size:9.5px;letter-spacing:.8px;text-transform:uppercase}
.features svg{width:16px;height:16px;flex:none}

/* inside middle */
.panel--why{background:var(--white)}
.panel--why .label-stack{position:absolute;left:14px;top:268px}
.why-text{position:absolute;left:18px;right:18px;top:318px;font-size:7.2px;line-height:1.4}
.why-text p{margin-bottom:6px}
.why-text strong{font-weight:600}
.why-contact{position:absolute;left:18px;top:478px;list-style:none;font-size:9.5px;line-height:1.45}
.why-contact li{display:flex;align-items:center;gap:8px}
.why-contact svg{width:10px;height:10px;flex:none}

/* inside right */
.panel--studio{background:var(--grey);color:var(--white)}
.panel--studio .label-stack{position:absolute;left:14px;top:16px}
.studio-text{position:absolute;left:16px;right:14px;top:46px;font-size:7.1px;line-height:1.4}
.studio-text p{margin-bottom:6px}
.panel--studio .photo{left:0;right:0;bottom:0;height:270px;background:linear-gradient(160deg,#d8d2cc 0%,#b79c84 45%,#4b4547 100%)}
</style>
</head>
<body>

<section class="spread spread--outside" aria-label="Flyer Außenseite">
  <article class="panel panel--wig">
    <p class="intro">Sind Sie an einer Perücke interessiert die augenscheinlich keinen Unterschied zu gewachsenem Haar aufweist?</p>
    <div class="label-stack">
      <span class="label">Dann sind Sie bei uns an der</span>
      <span class="label">richtigen Adresse</span>
    </div>
    <ul class="benefits">
      <li><svg viewBox="0 0 16 16"><circle cx="8" cy="7" r="5" fill="none" stroke="#6f7477" stroke-width="1.6"/><circle cx="8" cy="7" r="2" fill="#6f7477"/><path d="M5 11l-1 4 4-2 4 2-1-4" fill="#6f7477"/></svg><span>Die langjährige Erfahrung im Zweithaar Bereich von Friseurmeisterin Marion Kessing verspricht Ihnen optimale Beratung und ein individuell auf Sie abgestimmtes Produkt.</span></li>
      <li><svg viewBox="0 0 16 16"><rect x="1" y="5" width="4" height="10" fill="#6f7477"/><rect x="6" y="3" width="4" height="12" fill="#8d9194"/><rect x="11" y="1" width="4" height="14" fill="#6f7477"/></svg><span>Bei uns erhalten Sie Zugriff auf verschiedene Modelle im gesamten Preisspektrum.</span></li>
      <li><svg viewBox="0 0 16 16"><rect x="2" y="1" width="12" height="14" fill="none" stroke="#6f7477" stroke-width="1.6"/><path d="M5 5h6M5 8h6M5 11h4" stroke="#6f7477" stroke-width="1.4"/></svg><span>Liegt eine von Ihrem Arzt attestierte Erkrankung vor, übernimmt Ihre Krankenkasse höchstwahrscheinlich die Kosten für Ihr Zweithaar. Die Formalitäten dazu erledigen wir gerne für Sie um Ihnen unnötigen Stress zu ersparen.</span></li>
    </ul>
    <div class="photo" role="img" aria-label="Foto: junger Mann mit vollem Haar sitzt lächelnd vor einer dunklen Holzwand"></div>
  </article>

  <article class="panel panel--contact">
    <div class="label-stack">
      <span class="label">Kostenlos und unverbindlich</span>
      <span class="label">beraten lassen!</span>
    </div>
    <div class="brand">Lorin</div>
    <div class="brand-sub">Falk</div>
    <ul class="contact">
      <li><svg viewBox="0 0 10 10"><circle cx="5" cy="3" r="2.2" fill="#fff"/><path d="M1 10a4 4 0 0 1 8 0z" fill="#fff"/></svg><b>LORIN Falk | Marion Kessing</b><br>Lindenallee 14<br>44135 Dortmund</li>
      <li><svg viewBox="0 0 10 10"><path d="M2 1l2 2-1 1.5a6 6 0 0 0 2.5 2.5L7 6l2 2-1.5 1.5C4.5 9 1 5.5.5 2.5z" fill="#fff"/></svg><b>Festnetz:</b> 0231 48 62 19 05<br><b>Mobil:</b> 0170 33 84 261</li>
      <li><svg viewBox="0 0 10 10"><rect x="0.5" y="2" width="9" height="6.5" fill="#fff"/><path d="M.5 2l4.5 3.5L9.5 2" fill="none" stroke="#7c8184"/></svg><b>EMail:</b> info@lorin-falk.de</li>
      <li><svg viewBox="0 0 10 10"><circle cx="5" cy="5" r="4.3" fill="none" stroke="#fff"/><ellipse cx="5" cy="5" rx="1.8" ry="4.3" fill="none" stroke="#fff"/><path d="M.7 5h8.6" stroke="#fff"/></svg><b>www.lorin-falk.de</b></li>
    </ul>
    <div class="hours">
      <h3>Öffnungszeiten</h3>
      <dl>
        <dt>Montag:</dt><dd>geschlossen</dd>
        <dt>Dienstag - Freitag:</dt><dd>09:30h - 18:00h</dd>
        <dt>Samstag:</dt><dd>nach Terminvereinbarung</dd>
      </dl>
    </div>
  </article>

  <article class="panel panel--cover">
    <div class="brand">Lorin</div>
    <div class="brand-sub">Falk</div>
    <h1 class="cover-title">Perücken <small>und</small><br>Toupets!</h1>
    <p class="cover-sub">individuell nach Ihren Bedürfnissen!</p>
    <div class="photo" role="img" aria-label="Foto: Frau mit langem, welligem, hellbraunem Haar"></div>
    <div class="label-stack">
      <span class="label">Jetzt Termin</span>
      <span class="label">vereinbaren</span>
    </div>
    <p class="cover-web">www.lorin-falk.de</p>
  </article>
</section>

<section class="spread spread--inside" aria-label="Flyer Innenseite">
  <div class="photo photo--hero" role="img" aria-label="Foto: Frau mit wehendem, rotem Haar vor dunklem Hintergrund"></div>

  <article class="panel panel--toupet">
    <div class="questions">
      <span class="label">Leiden Sie an übermässigem<br>Haarausfall?</span>
      <span class="label">Fühlen Sie sich nicht mehr 100%<br>wohl damit?</span>
      <span class="label">Möchten Sie Ihre Attraktivität<br>und Ihr Wohlbefinden steigern</span>
      <span class="label">Dann sind Sie bei uns<br>genau richtig!</span>
    </div>
    <div class="fit">
      <p>Wir passen Ihr Toupet individuell und auf Ihre Bedürfnisse an:</p>
      <ul class="features">
        <li><svg viewBox="0 0 16 16"><rect x="1" y="6" width="4" height="9" fill="#fff"/><rect x="6" y="4" width="4" height="11" fill="#dcdcdc"/><rect x="11" y="2" width="4" height="13" fill="#fff"/></svg>Farbe</li>
        <li><svg viewBox="0 0 16 16"><path d="M2 4h10l2 3-2 3H2z" fill="#fff"/><circle cx="5" cy="7" r="1.2" fill="#7c8184"/></svg>Grauanteil</li>
        <li><svg viewBox="0 0 16 16"><rect x="1" y="6" width="14" height="5" fill="#fff"/><path d="M4 6v2M7 6v3M10 6v2M13 6v3" stroke="#7c8184"/></svg>Grösse</li>
        <li><svg viewBox="0 0 16 16"><circle cx="4" cy="12" r="2.3" fill="none" stroke="#fff" stroke-width="1.4"/><circle cx="12" cy="12" r="2.3" fill="none" stroke="#fff" stroke-width="1.4"/><path d="M5.5 10.5L12 2M10.5 10.5L4 2" stroke="#fff" stroke-width="1.4"/></svg>Styling</li>
      </ul>
    </div>
  </article>

  <article class="panel panel--why">
    <div class="label-stack">
      <span class="label">Warum sollten Sie in unser</span>
      <span class="label">Studio kommen?</span>
    </div>
    <div class="why-text">
      <p>Mit unserer Befestigungsmethode sind Sie sehr flexibel - starker Halt für jede Situation und auf Wunsch auch abnehmbar zum Beispiel nachts beim Schlafen.</p>
      <p>Der große Vorteil unserer Befestigungsmethode liegt darin, dass Sie diese selbst umsetzen können und somit nicht jeden Monat das Studio zur Neubefestigung aufsuchen müssen. <strong>Das spart Ihnen Zeit und Geld.</strong></p>
      <p>Wir können Ihnen Toupets und Perücken in allen Preisklassen anbieten, in verschiedenen Farben, auf Wunsch mit Grauanteil passend zum Alter des Trägers.</p>
      <p>Unsere Friseurmeisterin Frau Kessing berät Sie gerne, natürlich unverbindlich und kostenlos.</p>
    </div>
    <ul class="why-contact">
      <li><svg viewBox="0 0 10 10"><path d="M2 1l2 2-1 1.5a6 6 0 0 0 2.5 2.5L7 6l2 2-1.5 1.5C4.5 9 1 5.5.5 2.5z" fill="#55595c"/></svg>0231 - 48 62 19 05</li>
      <li><svg viewBox="0 0 10 10" style="visibility:hidden"></svg>Mobil: 0170 33 84 261</li>
      <li><svg viewBox="0 0 10 10"><rect x="0.5" y="2" width="9" height="6.5" fill="#55595c"/><path d="M.5 2l4.5 3.5L9.5 2" fill="none" stroke="#fff"/></svg>info@lorin-falk.de</li>
      <li><svg viewBox="0 0 10 10"><circle cx="5" cy="5" r="4.3" fill="none" stroke="#55595c"/><ellipse cx="5" cy="5" rx="1.8" ry="4.3" fill="none" stroke="#55595c"/><path d="M.7 5h8.6" stroke="#55595c"/></svg>www.lorin-falk.de</li>
    </ul>
  </article>

  <article class="panel panel--studio">
    <div class="label-stack">
      <span class="label">Wir beraten Sie gerne!</span>
    </div>
    <div class="studio-text">
      <p>Unser Zweithaar Studio befindet sich im ersten Obergeschoss eines barrierefrei zugänglichen Ärztehauses. Es arbeiten mehrere Praxen in dem Gebäude, daher können Sie völlig unauffällig unser Studio erreichen.</p>
      <p>Frau Kessing freut sich Sie in unserem Studio begrüßen zu dürfen.</p>
      <p>Während Ihres Termins sind Sie der einzige Kunde vor Ort, es werden keine Paralleltermine vereinbart. Ein Sichtschutz trennt den Arbeitsbereich vom Eingangsbereich im Studio für den Fall dass spontan ein Kunde z.B. Zubehör abholen möchte.</p>
      <p>Für alle Kunden die mit den öffentlichen Verkehrsmitteln anreisen haben wir auch gute Nachrichten. Die nächste Bahn und U-Bahn Station befinden sich nur 2-3 Gehminuten von uns entfernt.</p>
    </div>
    <div class="photo" role="img" aria-label="Foto: Friseurin schneidet einer Kundin mit langem blondem Haar die Haare"></div>
  </article>
</section>

</body>
</html>
```